Business card for Bright Keystone

Front (space for each) - Name, title, qualifications, mobile number, email address, website, name/logo,
Back - Business name/logo and slogan "your dream is our vision" underneath,
in small writing underneath need ABN number, CRN number, ACL number
Target Market(s)
First Home Buyers
Industry/Entity Type
Finance
Contact Information for Business Card
Requirements
Must have
- Front (space for each) - Name, title, qualifications, mobile number, email address, website, name/logo,

```html
<!DOCTYPE html>
<html lang="en">
<head>
<meta charset="UTF-8">
<title>Bright Keystone — Business Card</title>
<link href="https://fonts.googleapis.com/css2?family=Poppins:wght@400;500;600;700&family=Dancing+Script:wght@500&display=swap" rel="stylesheet">
<style>
  :root {
    --page-bg: #e9e6e1;
    --navy: #354052;
    --paper: #f7f7f7;
    --ink: #1c1c1c;
    --white: #ffffff;
    --lime: #8cc63f;
    --green: #1f9a4a;
    --teal: #1fae8a;
    --orange: #f08a3a;
  }
  * { box-sizing: border-box; margin: 0; padding: 0; }
  html, body { width: 1200px; height: 1091px; overflow: hidden; }
  body {
    background: var(--page-bg);
    font-family: "Poppins", sans-serif;
    position: relative;
  }
  .card {
    position: absolute;
    left: 190px;
    width: 820px;
    height: 468px;
    border-radius: 4px;
    box-shadow: 0 8px 24px rgba(0,0,0,0.18);
    overflow: hidden;
  }
  /* Back */
  .card-back { top: 50px; background: var(--navy); color: var(--white); text-align: center; }
  .brand-back {
    position: absolute; top: 140px; left: 0; right: 0;
    font-weight: 700; font-size: 44px; letter-spacing: 3px; text-transform: uppercase;
  }
  .slogan {
    position: absolute; top: 220px; left: 0; right: 0;
    font-family: "Dancing Script", cursive; font-size: 52px; color: var(--lime);
  }
  .registrations {
    position: absolute; top: 320px; left: 0; right: 0;
    font-size: 16px; letter-spacing: 1px; color: var(--white);
  }
  .registrations .label { color: var(--orange); font-weight: 600; }
  .registrations .sep { margin: 0 18px; color: var(--orange); }

  /* Front */
  .card-front { top: 572px; background: var(--paper); color: var(--ink); }
  .brand-front {
    position: absolute; top: 58px; right: 60px;
    font-weight: 700; font-size: 40px; letter-spacing: 3px; text-transform: uppercase; color: var(--ink);
  }
  .divider {
    position: absolute; top: 210px; left: 330px; right: 60px;
    height: 2px; background: var(--green);
  }
  .holder { position: absolute; left: 60px; top: 245px; }
  .holder-name { font-weight: 600; font-size: 42px; line-height: 1.1; white-space: nowrap; }
  .holder-title, .holder-quals { font-size: 17px; font-weight: 500; line-height: 1.5; }
  .holder-title { margin-top: 8px; }
  .contact-list { position: absolute; top: 240px; list-style: none; font-size: 16px; font-weight: 500; }
  .contact-list li { display: flex; align-items: center; gap: 12px; line-height: 1.9; white-space: nowrap; }
  .contact-list svg { width: 16px; height: 16px; flex: none; }
  .contacts-phone { left: 340px; }
  .contacts-web { left: 520px; }
</style>
</head>
<body>

<section class="card card-back" aria-label="Card back">
  <div class="brand-back">Bright Keystone</div>
  <p class="slogan">your dream is our vision</p>
  <p class="registrations">
    <span class="label">ABN:</span> 123456<span class="sep">|</span><span class="label">CRN:</span> 123456<span class="sep">|</span><span class="label">ACL:</span> 123456
  </p>
</section>

<section class="card card-front" aria-label="Card front">
  <div class="brand-front">Bright Keystone</div>
  <div class="divider"></div>

  <div class="holder">
    <p class="holder-name">Liam Carter</p>
    <p class="holder-title">Business Executive</p>
    <p class="holder-quals">B.Sc(Phy), MBA(Finance)</p>
  </div>

  <ul class="contact-list contacts-phone">
    <li>
      <svg viewBox="0 0 16 16"><path fill="#1f9a4a" d="M3 1l3 3-1.5 2a9 9 0 0 0 5.5 5.5L12 10l3 3-2 2C7 15 1 9 1 3z"/></svg>
      555 014-2283
    </li>
    <li>
      <svg viewBox="0 0 16 16"><rect x="4" y="1" width="8" height="14" rx="1.5" fill="none" stroke="#1f9a4a" stroke-width="1.6"/><circle cx="8" cy="12.5" r="0.9" fill="#1f9a4a"/></svg>
      555 014-2283
    </li>
  </ul>

  <ul class="contact-list contacts-web">
    <li>
      <svg viewBox="0 0 16 16"><rect x="1" y="3" width="14" height="10" rx="1" fill="#1fae8a"/><path d="M1.5 4l6.5 5 6.5-5" fill="none" stroke="#fff" stroke-width="1.3"/></svg>
      info@brightkeystone.com
    </li>
    <li>
      <svg viewBox="0 0 16 16"><circle cx="8" cy="8" r="6.5" fill="none" stroke="#1fae8a" stroke-width="1.5"/><path d="M1.5 8h13M8 1.5c-3 3.5-3 9.5 0 13M8 1.5c3 3.5 3 9.5 0 13" fill="none" stroke="#1fae8a" stroke-width="1.2"/></svg>
      www.brightkeystone.com
    </li>
  </ul>
</section>

</body>
</html>
```